Plumber needs a business card

I need a new business card for my plumbing business. I dont have a logo at the moment but I want business cards that are simple but very professional. I want to look like
Name: Mitch Dorley
Address: (just make one up)
Phone: 0455 318 726
Email: mitch@dorleymail.com
Colors to use:
Blacks, blues, silvers

```html
<!DOCTYPE html>
<html lang="en">
<head>
<meta charset="utf-8">
<title>Mitch Dorley Plumbing Service – Business Card</title>
<link rel="stylesheet" href="https://fonts.googleapis.com/css2?family=Alice&family=Arimo:wght@400&display=swap">
<style>
  :root {
    --page-bg: #e9eaec;
    --card-black: #000000;
    --panel-grey: #1c1c1e;
    --brand-blue: #2f8fd0;
    --silver: #c9ccd1;
    --silver-dark: #8a8d92;
    --text-white: #f2f2f2;
    --icon-violet: #6a4cf0;
    --icon-blue: #2f8fd0;
    --art-blue-light: #7cc2ee;
    --art-blue-dark: #1f5f96;
  }
  * { margin: 0; padding: 0; box-sizing: border-box; }
  html, body {
    width: 1200px;
    height: 1200px;
    overflow: hidden;
    background: var(--page-bg);
  }
  .canvas {
    position: relative;
    width: 1200px;
    height: 1200px;
  }
  .business-card {
    position: absolute;
    left: 80px;
    top: 330px;
    width: 1040px;
    height: 540px;
    background: var(--card-black);
    box-shadow: 0 18px 40px rgba(0, 0, 0, 0.25);
    overflow: hidden;
  }
  .brand-name {
    position: absolute;
    left: 58px;
    top: 48px;
    font-family: "Alice", serif;
    font-size: 58px;
    font-weight: 400;
    line-height: 1;
    color: var(--brand-blue);
  }
  .brand-trade {
    position: absolute;
    left: 58px;
    top: 134px;
    width: 330px;
    font-family: "Alice", serif;
    font-size: 34px;
    line-height: 1;
    color: var(--silver);
    letter-spacing: 0.5px;
    padding-bottom: 14px;
  }
  .brand-trade::after {
    content: "";
    position: absolute;
    left: 0;
    right: 0;
    bottom: 0;
    height: 3px;
    background: linear-gradient(90deg, var(--silver-dark), var(--silver) 45%, var(--silver-dark) 80%, transparent);
  }
  .contact-panel {
    position: absolute;
    left: 36px;
    top: 254px;
    width: 500px;
    height: 170px;
    border-radius: 10px;
    background: radial-gradient(ellipse at center, var(--panel-grey) 40%, transparent 75%);
  }
  .contact-list {
    position: absolute;
    left: 60px;
    top: 268px;
    list-style: none;
    font-family: "Arimo", sans-serif;
    font-size: 26px;
    letter-spacing: 3px;
    color: var(--text-white);
  }
  .contact-item {
    display: flex;
    align-items: center;
    gap: 18px;
    height: 46px;
    white-space: nowrap;
  }
  .contact-icon { width: 30px; height: 30px; flex: none; }
  .service-illustration {
    position: absolute;
    left: 570px;
    top: 30px;
    width: 420px;
    height: 360px;
    border-radius: 12px;
    background: linear-gradient(160deg, var(--art-blue-light), var(--art-blue-dark) 70%, #e8eef3);
  }
  .tagline {
    position: absolute;
    left: 0;
    right: 0;
    top: 446px;
    text-align: center;
    font-family: "Alice", serif;
    font-size: 40px;
    line-height: 1.2;
    letter-spacing: 1px;
    color: var(--text-white);
  }
</style>
</head>
<body>
<main class="canvas">
  <section class="business-card" aria-label="Mitch Dorley Plumbing Service business card">
    <h1 class="brand-name">Mitch Dorley</h1>
    <p class="brand-trade">Plumbing Service</p>

    <div class="contact-panel"></div>
    <ul class="contact-list">
      <li class="contact-item">
        <svg class="contact-icon" viewBox="0 0 30 30" aria-hidden="true">
          <rect width="30" height="30" rx="7" fill="var(--icon-violet)"/>
          <path d="M10 7c1 0 1.6.3 2 1.2l1.2 2.8c.3.8 0 1.4-.6 1.9l-1 .8c.9 2 2.5 3.6 4.5 4.6l.8-1c.5-.6 1.2-.8 1.9-.5l2.8 1.2c.8.4 1.2 1 1.1 2l-.3 1.6c-.2 1-1 1.6-2 1.6C13.8 23.8 6.2 16.2 6.4 9.3c0-1 .7-1.8 1.7-2z" fill="#fff"/>
        </svg>
        <span>0455 318 726</span>
      </li>
      <li class="contact-item">
        <svg class="contact-icon" viewBox="0 0 30 30" aria-hidden="true">
          <rect x="2" y="6" width="26" height="18" rx="2" fill="#f4f4f4"/>
          <path d="M3 8l12 9 12-9" fill="none" stroke="#d9443a" stroke-width="2.6"/>
        </svg>
        <span>mitch@dorleymail.com</span>
      </li>
      <li class="contact-item">
        <svg class="contact-icon" viewBox="0 0 30 30" aria-hidden="true">
          <path d="M15 3c-5 0-9 3.8-9 8.8C6 18.5 15 27 15 27s9-8.5 9-15.2C24 6.8 20 3 15 3z" fill="var(--icon-blue)"/>
          <circle cx="15" cy="12" r="3.6" fill="#fff"/>
        </svg>
        <span>14 Kellan St, Brookvale</span>
      </li>
    </ul>

    <div class="service-illustration" role="img" aria-label="Illustration of a plumber in cap and overalls holding a large pipe wrench"></div>

    <p class="tagline">Service, Repair and Installation</p>
  </section>
</main>
</body>
</html>
```